(front)
PeakWay Logo
Keeping You Competitive
In the ever-changing world of healthcare, you need a partner who can keep you current and ensure you are getting the most out of your rehabilitation services.
(Inside cover)
Our Mission
Quality-Recruitment, management, continued education, research and technology
Compliance-Accuracy of service within practice guidelines and federal regulations
Expertise-Audit and compliance, out-patient, clinical programs, education and career development, evidence based practice and speech and dysphagia programs
Ethics-Integrity and social responsiblity
Vision-Top set the standard of performance and practice within the rehabilitation industry
We're here to help!
-Improve efficiencies
-Optimize outcomes
-Audit for compliance
(Inside Back Cover)
PeakWay Therapy Logo
peakwaytherapy-example.net
Keeping You Competitive
Call Us Today- 555-318-4402
We're a professional team of Physical, Occupational, Speech and Therapist Assistants who work together to bring you excellent rehabilitation services. Our knowledge, enthusiasm and drive allow us to be leaders in the healthcare industry.
(Back Cover)
Full Service Contract: We do it all....recruit, employ, teach and audit.
Management Contract: We help you recruit and manage. The manager works for us, the therapists work for you.
Call us for a free audit. 555-318-4402
Industry/Entity Type
Healthcare
Look and feel
Each slider illustrates characteristics of the customer's brand and the style your logo design should communicate.

```html
<!DOCTYPE html>
<html lang="en">
<head>
<meta charset="utf-8">
<title>PeakWay Therapy Brochure</title>
<link href="https://fonts.googleapis.com/css2?family=Asap+Condensed:wght@400;500;600;700&display=swap" rel="stylesheet">
<style>
:root{
  --blue:#1d4f9c;
  --gold:#9a8350;
  --gold-line:#9b8552;
  --sheet-edge:#d6d6d6;
  --sheet-light:#ffffff;
  --sheet-shade:#e2e2e2;
  --fold:#555;
}
*{margin:0;padding:0;box-sizing:border-box}
html,body{width:891px;height:1200px;overflow:hidden;background:#fff}
body{position:relative;font-family:"Asap Condensed",sans-serif}
.spread{
  position:absolute;left:59px;width:775px;height:497px;
  border:1px solid var(--sheet-edge);
  background:radial-gradient(ellipse at 55% 45%,var(--sheet-light) 0%,#f2f2f2 45%,var(--sheet-shade) 100%);
  box-shadow:0 0 30px rgba(0,0,0,.12);
  overflow:hidden;
}
.spread--outside{top:64px}
.spread--inside{top:626px;height:496px}
.fold{position:absolute;left:446px;width:0;border-left:1px dashed var(--fold)}
.fold--outside{top:52px;height:530px}
.fold--inside{top:614px;height:530px}
.shape{position:absolute;left:0;top:0}
.panel-text{position:absolute;color:var(--gold)}
.blue{color:var(--blue)}
.contracts{left:15px;top:20px;width:340px;font-size:16.5px;line-height:22px}
.contracts p{margin-bottom:8px}
.audit-call{font-size:17px;margin-top:12px}
.audit-call strong{font-size:23px;font-weight:700;margin-left:4px}
.brand{font-weight:700;color:var(--blue);letter-spacing:.2px;display:flex;align-items:center;gap:6px}
.brand::after{content:"";width:12px;height:12px;border-radius:50%;background:var(--gold)}
.brand--front{position:absolute;left:545px;top:28px;font-size:27px}
.front-copy{left:445px;top:133px;width:300px}
.front-copy h1{font-size:25px;font-weight:500;color:var(--blue);line-height:30px;margin-bottom:4px}
.front-copy p{font-size:16.5px;line-height:24px}
.photo-strip{position:absolute;left:527px;top:356px;width:248px;height:128px;display:flex;gap:3px;border-radius:10px 0 0 10px;overflow:hidden}
.photo{flex:1}
.photo--a{background:linear-gradient(160deg,#c9c3b8,#5f9ac8 70%,#8ab3cf)}
.photo--b{background:linear-gradient(160deg,#e9eef2,#b9c7d3 50%,#a04a4a)}
.photo--c{background:linear-gradient(160deg,#dfe6ea,#9fb3a7 55%,#c8c2b8)}
.mission{left:18px;top:20px;width:385px;font-size:14px;line-height:20px}
.mission h2{font-size:17px;font-weight:700;color:var(--blue);margin-bottom:6px}
.mission p{margin-bottom:14px}
.mission b{font-weight:700}
.help{left:20px;top:372px;font-size:17px;line-height:25px;color:var(--blue)}
.help h3{font-size:19px;font-weight:700;margin-bottom:2px}
.help ul{list-style:none}
.help li::before{content:"• "}
.contact-card{position:absolute;left:428px;top:118px;width:360px;height:316px;background:#fff;border-radius:10px}
.brand--back{position:absolute;left:26px;top:20px;font-size:24px}
.contact{position:absolute;left:26px;top:94px;width:310px;color:var(--gold)}
.contact .url{font-size:22px;font-weight:700;color:var(--blue);margin-bottom:8px}
.contact .tag{font-size:14px;line-height:20px}
.contact .call{font-size:14px}
.contact .call strong{font-size:23px;font-weight:700}
.contact .about{margin-top:10px;font-size:13px;line-height:22px;font-weight:500;color:var(--blue)}
</style>
</head>
<body>

<section class="spread spread--outside">
  <svg class="shape" width="775" height="497" viewBox="0 0 775 497" aria-hidden="true">
    <path d="M312,0 C410,88 590,112 775,113 L775,0 Z" fill="#fff"/>
    <path d="M312,0 C410,88 590,112 775,113" fill="none" stroke="var(--gold-line)" stroke-width="4"/>
  </svg>

  <div class="panel-text contracts">
    <p><span class="blue">Full Service Contract:</span> We do it all....recruit, employ, teach and audit.</p>
    <p><span class="blue">Management Contract:</span> We help you recruit and manage. The manager works for us, the therapists work for you.</p>
    <p class="audit-call blue">Call us for a free audit <strong>555-318-4402</strong></p>
  </div>

  <div class="brand brand--front">PeakWay Therapy</div>

  <div class="panel-text front-copy">
    <h1>Keeping You Competitive</h1>
    <p>In the ever-changing world of healthcare, you need a partner who can keep you current and ensure you are getting the most out of your rehabilitation services.</p>
  </div>

  <div class="photo-strip">
    <div class="photo photo--a" role="img" aria-label="Photo of a smiling patient during physical therapy exercise"></div>
    <div class="photo photo--b" role="img" aria-label="Photo of a therapist working with a patient"></div>
    <div class="photo photo--c" role="img" aria-label="Photo of an older patient lifting hand weights with a therapist"></div>
  </div>
</section>
<div class="fold fold--outside"></div>

<section class="spread spread--inside">
  <svg class="shape" width="775" height="496" viewBox="0 0 775 496" aria-hidden="true">
    <path d="M0,320 C150,345 280,400 340,496 L0,496 Z" fill="#fff"/>
    <path d="M0,320 C150,345 280,400 340,496" fill="none" stroke="var(--gold-line)" stroke-width="4"/>
  </svg>

  <div class="panel-text mission">
    <h2>Our Mission</h2>
    <p><b>Quality-</b> Recruitment, management, continued education, research and technology</p>
    <p><b>Compliance-</b> Accuracy of service within practice guidelines and federal regulations</p>
    <p><b>Expertise-</b> Audit and compliance, out-patient, clinical programs, education and career development, evidence based practice and speech and dysphagia programs</p>
    <p><b>Ethics-</b> Integrity and social responsiblity</p>
    <p><b>Vision-</b> Top set the standard of performance and practice within the rehabilitation industry</p>
  </div>

  <div class="panel-text help">
    <h3>We're here to help!</h3>
    <ul>
      <li>Improve efficiencies</li>
      <li>Optimize outcomes</li>
      <li>Audit for compliance</li>
    </ul>
  </div>

  <div class="contact-card">
    <div class="brand brand--back">PeakWay Therapy</div>
    <div class="contact">
      <div class="url">peakwaytherapy-example.net</div>
      <div class="tag">Keeping You Competitive</div>
      <div class="call">Call Us Today <strong>555-318-4402</strong></div>
      <p class="about">We're a professional team of Physical, Occupational, Speech and Therapist Assistants who work together to bring you excellent rehabilitation services. Our knowledge, enthusiasm and drive allow us to be leaders in the healthcare industry.</p>
    </div>
  </div>
</section>
<div class="fold fold--inside"></div>

</body>
</html>
```